50 years of Beat (birthday party)

I need a flyer that I can send to all guests as ChatLoop.
Also as a digital file (e.g. PDF). Thanks!
Occasion: Beat's 50th birthday
It's a birthday party for family and friends
Location: Marquee at the football field, 7345 Felsbach
Live music
Bar pub
Murrow
Date: Saturday, May 25, 2024
Time: from 2 p.m. until open-end
Flexible participation - come and go as you please
Registration or deregistration: ChatLoop on 078 - 312 65 17

Please create a flyer as an invitation. I want an Irish rock style with a touch of “Schlager” :-). There should be a real party.
Attention: no heavy metal style!!
It would be cool if a rock guitar and/or microphone were included.
Otherwise, I'm free and happy to be surprised. The flyer should not be too childish or youthful. There are practically no children at the event.

Additionally, please send a simpler flyer than “Save the date”.
Just the date and occasion.
Without place, time and registration.
With the note: Update follows...
The design is the same as the flyer with registration.
Updates

It would be cool if the Murrow logo was visible too.
A whiskey glass would also be possible.
Balloons are not absolutely necessary - it looks like a children's party.
Please make the flyers rocky.

Target Market(s)

Family & Friends

Industry/Entity Type

look

Font styles to use
Other font styles liked:
• rockig

Colors

Designer to choose colors to be used in the design.

Requirements
Must have
• Irish rock design
Nice to have
• Rock guitar would be cool
Should not have
• comics

```html
<!DOCTYPE html>
<html lang="en">
<head>
<meta charset="utf-8">
<title>Beat's 50th Birthday – Invitation</title>
<link href="https://fonts.googleapis.com/css2?family=Lobster&family=Oswald:wght@500;600&display=swap" rel="stylesheet">
<style>
  :root{
    --page:#c8c8c8;
    --night:#1d1430;
    --violet:#9a34d6;
    --magenta:#d22be0;
    --plum:#8c2a68;
    --disc:#45294f;
    --ring:#ffffff;
    --white:#ffffff;
    --yellow:#f7e824;
    --cream:#f8ec8a;
    --pink:#ff2f9c;
    --gold:#f5c21b;
    --script:"Lobster", cursive;
    --condensed:"Oswald", sans-serif;
  }
  *{margin:0;padding:0;box-sizing:border-box}
  html,body{width:980px;height:1200px;overflow:hidden;background:var(--page)}
  .flyer{
    position:absolute;left:79px;top:19px;width:822px;height:1162px;overflow:hidden;
    background:
      radial-gradient(ellipse 60% 45% at 10% 30%, rgba(190,90,255,.75), transparent 70%),
      radial-gradient(ellipse 50% 40% at 95% 10%, rgba(230,40,240,.85), transparent 70%),
      linear-gradient(180deg, var(--violet) 0%, #7a2ab8 45%, #3a1a55 70%, var(--night) 100%);
  }
  .flyer svg.backdrop{position:absolute;inset:0}
  .art{position:absolute}
  .line{position:absolute;left:0;width:100%;text-align:center;white-space:nowrap;line-height:1}
  .script{font-family:var(--script);font-weight:400}
  .caps{font-family:var(--condensed);font-variant:small-caps;font-weight:500}
  .name{top:192px;font-size:104px;color:var(--white)}
  .occasion{top:316px;font-size:82px;color:var(--yellow)}
  .occasion sup{font-size:42px;vertical-align:34px}
  .tagline{top:433px;font-size:29px;color:var(--white);letter-spacing:.2px}
  .weekday{top:487px;font-size:41px;color:var(--cream)}
  .date{top:544px;font-size:52px;color:var(--cream);font-family:var(--condensed);font-weight:600}
  .highlights{top:752px;font-size:58px;color:var(--white)}
  .highlights .dot{color:var(--yellow);font-size:32px;vertical-align:5px;margin:0 6px}
  .participation{top:827px;font-size:31px;color:var(--white)}
  .hours{top:876px;font-size:43px;color:var(--yellow);font-weight:600}
  .location{
    position:absolute;left:120px;top:952px;width:580px;height:45px;
    border:1.5px solid var(--gold);border-radius:23px;
    display:flex;align-items:center;justify-content:center;
    font-size:27px;color:var(--yellow);white-space:nowrap;
  }
  .location .place{color:var(--pink);margin-left:6px}
  .signup{top:1016px;font-size:34px;color:var(--white)}
  .contact{top:1055px;font-size:31px;color:var(--yellow);font-weight:600}
</style>
</head>
<body>
<main class="flyer">
  <svg class="backdrop" width="822" height="1162" viewBox="0 0 822 1162" aria-hidden="true">
    <g opacity=".35" fill="#e9b8ff">
      <polygon points="0,330 430,470 430,480 0,350"/>
      <polygon points="0,420 420,520 420,528 0,440"/>
      <polygon points="0,520 420,580 420,586 0,540"/>
    </g>
    <path d="M170,20 C240,-20 600,-10 700,40 C790,90 800,260 740,330 C700,380 620,330 560,300 C420,230 250,330 160,260 C110,220 120,60 170,20Z" fill="var(--plum)" opacity=".85"/>
    <path d="M650,0 L822,0 L822,260 C770,250 720,170 660,90 C640,60 640,20 650,0Z" fill="#c02fa8" opacity=".7"/>
    <circle cx="410" cy="395" r="340" fill="#5a1c8e" opacity=".55"/>
    <g stroke-linecap="round" stroke-width="26" fill="none">
      <line x1="140" y1="640" x2="230" y2="560" stroke="#f59a2a" opacity=".9"/>
      <line x1="200" y1="690" x2="300" y2="600" stroke="#d9365d" opacity=".8"/>
      <line x1="300" y1="720" x2="380" y2="650" stroke="#c2306a" opacity=".7"/>
      <line x1="700" y1="380" x2="760" y2="330" stroke="#d9365d" opacity=".7"/>
      <line x1="120" y1="520" x2="170" y2="480" stroke="#c2306a" opacity=".6"/>
    </g>
    <circle cx="410" cy="395" r="300" fill="var(--ring)"/>
    <circle cx="410" cy="395" r="268" fill="var(--disc)"/>
    <g fill="var(--gold)">
      <polygon points="108,20 118,40 96,40"/>
      <polygon points="95,115 128,172 65,172"/>
      <polygon points="752,40 780,85 725,85"/>
      <polygon points="300,15 315,30 300,30" transform="rotate(-20 305 22)"/>
      <polygon points="725,570 745,605 705,605"/>
      <polygon points="15,960 32,990 -2,990"/>
    </g>
    <g fill="#c9a3e0" opacity=".8">
      <polygon points="782,452 795,470 770,470"/>
      <polygon points="748,592 768,620 728,620"/>
    </g>
    <g fill="#ff7ae6" opacity=".5">
      <circle cx="665" cy="745" r="14"/><circle cx="700" cy="690" r="10"/>
      <circle cx="630" cy="875" r="12"/><circle cx="780" cy="425" r="10"/>
    </g>
    <circle cx="780" cy="590" r="30" fill="#3b3bd9" opacity=".55"/>
    <circle cx="245" cy="930" r="30" fill="#3b3bd9" opacity=".4"/>
    <g stroke="#5b2a6e" stroke-width="2">
      <path d="M20 28h20M20 36h20M20 44h20M20 52h20M20 60h20M20 68h20M20 76h20M20 84h20M20 92h20M20 100h20M20 108h20M20 116h20M20 124h20M20 132h20M20 140h20M20 148h20M20 156h20M20 164h20M20 172h20M20 180h20M20 188h20M20 196h20M20 204h20M20 212h20M20 220h20M20 228h20M20 236h20M20 244h20M20 252h20M20 260h20M20 268h20M20 276h20M20 284h20M20 292h20"/>
    </g>
    <g stroke="var(--gold)" stroke-width="2">
      <path d="M780 868h20M780 876h20M780 884h20M780 892h20M780 900h20M780 908h20M780 916h20M780 924h20M780 932h20M780 940h20M780 948h20M780 956h20M780 964h20M780 972h20M780 980h20M780 988h20M780 996h20M780 1004h20M780 1012h20M780 1020h20M780 1028h20M780 1036h20M780 1044h20M780 1052h20M780 1060h20M780 1068h20M780 1076h20M780 1084h20M780 1092h20M780 1100h20M780 1108h20M780 1116h20M780 1124h20M780 1132h20"/>
    </g>
  </svg>

  <svg class="art" style="left:30px;top:55px" width="235" height="360" role="img" aria-label="Illustration of a red sunburst electric guitar">
    <rect x="95" y="0" width="30" height="230" rx="10" fill="#c9563a" transform="rotate(32 110 180)"/>
    <ellipse cx="80" cy="290" rx="78" ry="62" fill="#a82d12"/>
  </svg>
  <svg class="art" style="left:563px;top:415px" width="190" height="250" role="img" aria-label="Illustration of a violin with bow">
    <ellipse cx="75" cy="170" rx="62" ry="72" fill="#c8741f" transform="rotate(30 75 170)"/>
  </svg>
  <svg class="art" style="left:608px;top:95px" width="150" height="235" role="img" aria-label="Illustration of a bunch of party balloons">
    <ellipse cx="75" cy="100" rx="70" ry="95" fill="#c2478f" opacity=".85"/>
  </svg>
  <svg class="art" style="left:0;top:720px" width="100" height="250" role="img" aria-label="Illustration of party balloons">
    <ellipse cx="40" cy="125" rx="58" ry="120" fill="#c24a7e" opacity=".8"/>
  </svg>

  <h1 class="line script name">Beat's</h1>
  <p class="line script occasion">50<sup>th</sup> Birthday</p>
  <p class="line caps tagline">It's a birthday party for family and friends</p>
  <p class="line script weekday">Saturday</p>
  <p class="line date">MAY 25, 2024</p>

  <p class="line script highlights">Live music<span class="dot">●</span>Bar pub<span class="dot">●</span>Murrow</p>
  <p class="line caps participation">Flexible participation - come and go as you please</p>
  <p class="line caps hours">From 2 p.m. until open-end</p>
  <p class="location caps">Location:<span class="place">Marquee at the football field, 7345 Felsbach</span></p>
  <p class="line script signup">Registration or deregistration:</p>
  <p class="line caps contact">ChatLoop on 078 - 312 65 17</p>
</main>
</body>
</html>
```